Unique and original Business Card for Financial Services Business

I have moved premises and need to change the detail on my business card so thought now is a good time for a re-design. Looking for something professional and modern with colours to fit in with out logo. Like the idea of foil or embossing if that works but not a must have but I do want something that stands out and that I could not design myself.

Once business card is designed I will also be looking to get letterhead and flyers done but want the business card concept in place first.

The majority of designs I am receiving are generic and template based. I am looking for something unique and original. We have some great design elements in our logo, think outside the box and show me something that stands out from the crowd.

Target Market(s)

Business Professionals

Industry/Entity Type

Finance

Contact Information for Business Card

Name: Delia Norwood Phone 0473 958 162 Address PO Box 8617 Mossvale NSW 2389 Email info@steadyharbourfinancialservices.com.au website www.steadyharbourfinancialservices.com.au

Font styles to use
Other font styles liked:
• Ralway

Requirements
Should not have
• No black backgrounds please

```html
<!DOCTYPE html>
<html lang="en">
<head>
<meta charset="utf-8">
<title>Steady Harbour Financial Services – Business Card</title>
<link rel="stylesheet" href="https://fonts.googleapis.com/css2?family=Raleway:wght@400;700&display=swap">
<style>
  :root {
    --page-bg: #efece7;
    --card-bg: #e4e0da;
    --teal-deep: #0f4d55;
    --teal-mid: #16606a;
    --edge-line: #a9a39a;
    --ink: #4b5053;
    --text-light: #dcd8d1;
    --name-teal: #22907c;
  }
  * { box-sizing: border-box; margin: 0; padding: 0; }
  html, body {
    width: 1200px; height: 1047px; overflow: hidden;
    background: var(--page-bg);
    font-family: "Raleway", sans-serif;
  }
  .business-card {
    position: absolute; left: 100px; top: 250px;
    width: 1000px; height: 546px;
    border-radius: 22px; overflow: hidden;
    background: var(--card-bg);
    box-shadow: 0 18px 40px rgba(0,0,0,0.12);
  }
  .card-panel { position: absolute; inset: 0; width: 1000px; height: 546px; }
  .brand {
    position: absolute; left: 40px; top: 50px;
    display: flex; align-items: center; gap: 20px;
  }
  .brand-dot {
    width: 54px; height: 54px; border-radius: 50%;
    background: var(--teal-mid); flex: none;
  }
  .brand-name {
    font-weight: 400; font-size: 36px; line-height: 1.15;
    color: var(--ink); letter-spacing: 0.5px;
  }
  .holder-name {
    position: absolute; right: 40px; top: 248px;
    font-weight: 700; font-size: 33px; color: var(--name-teal);
  }
  .contact-list {
    position: absolute; right: 40px; top: 355px;
    list-style: none;
  }
  .contact-item {
    display: flex; justify-content: flex-end; align-items: center; gap: 18px;
    font-weight: 400; font-size: 22px; color: var(--text-light);
    height: 40px;
  }
  .contact-item.address { margin-bottom: 12px; }
  .contact-icon { width: 22px; height: 22px; flex: none; fill: var(--name-teal); }
</style>
</head>
<body>
  <div class="business-card">
    <svg class="card-panel" viewBox="0 0 1000 546" aria-hidden="true">
      <path d="M200,546 Q700,200 1000,170 L1000,546 Z" fill="var(--teal-deep)"/>
      <path d="M185,546 Q690,186 1000,156" fill="none" stroke="var(--edge-line)" stroke-width="3"/>
    </svg>

    <div class="brand">
      <span class="brand-dot"></span>
      <span class="brand-name">Steady Harbour<br>Financial Services</span>
    </div>

    <div class="holder-name">Delia Norwood</div>

    <ul class="contact-list">
      <li class="contact-item address">PO Box 8617 Mossvale NSW 2389
        <svg class="contact-icon" viewBox="0 0 24 24"><path d="M12 2a7 7 0 0 0-7 7c0 5 7 13 7 13s7-8 7-13a7 7 0 0 0-7-7zm0 9.5A2.5 2.5 0 1 1 12 6.5a2.5 2.5 0 0 1 0 5z"/></svg>
      </li>
      <li class="contact-item phone">0473 958 162
        <svg class="contact-icon" viewBox="0 0 24 24"><path d="M3 9c0-3 4-5 9-5s9 2 9 5v2h-5V9c-1-.6-2.4-1-4-1s-3 .4-4 1v2H3zM6 13h12l2 7H4z"/></svg>
      </li>
      <li class="contact-item email">info@steadyharbourfinancialservices.com.au
        <svg class="contact-icon" viewBox="0 0 24 24"><path d="M3 6h18v12H3zm2 2v.5l7 4.5 7-4.5V8l-7 4.5z"/></svg>
      </li>
      <li class="contact-item web">www.steadyharbourfinancialservices.com.au
        <svg class="contact-icon" viewBox="0 0 24 24"><circle cx="12" cy="12" r="9"/></svg>
      </li>
    </ul>
  </div>
</body>
</html>
```